Tawny Gnaw Guild Postcard Design

Need a postcard for this business. Go to tawnygnawguild.com to see the product we are selling. Here's another good postcard you can sample. https://www.marlowpinedesign.com/?lightbox=dataItem-je9eshek
Another one: http://blog.postwren.com/postcard-examples-from-popular-startups/

```html
<!DOCTYPE html>
<html lang="en">
<head>
<meta charset="utf-8">
<title>Tawny Gnaw Guild Postcard</title>
<link rel="stylesheet" href="https://fonts.googleapis.com/css2?family=Josefin+Slab:wght@600&family=Montserrat:wght@400;700;800;900&family=Oswald:wght@600;700&display=swap">
<style>
  :root {
    --page: #e7e5e1;
    --card: #f3f3f3;
    --ink: #333333;
    --green: #7dc242;
    --band: #8bc640;
    --blob: #a9cc9b;
    --bubble-line: #6e5649;
    --white: #ffffff;
  }
  * { margin: 0; padding: 0; box-sizing: border-box; }
  html, body { width: 1200px; height: 886px; overflow: hidden; background: var(--page); }
  .postcard {
    position: absolute; left: 30px; top: 76px;
    width: 1140px; height: 733px;
    background: var(--card);
    overflow: hidden;
    font-family: "Montserrat", sans-serif;
    color: var(--ink);
  }
  .shapes { position: absolute; inset: 0; }
  .dogs-photo {
    position: absolute; left: 150px; top: 25px; width: 262px; height: 512px;
    border-radius: 110px 110px 20px 20px;
    background: linear-gradient(180deg, #2a2522 0%, #5a4a3e 45%, #cdbba4 75%, #d9ccb8 100%);
  }
  .brand-seal {
    position: absolute; left: 54px; top: 372px; width: 228px; height: 228px;
    border-radius: 50%; background: var(--white);
    display: flex; align-items: center; justify-content: center;
  }
  .brand-seal .ring {
    width: 206px; height: 206px; border-radius: 50%;
    border: 4px solid #111;
    display: flex; align-items: center; justify-content: center; text-align: center;
  }
  .brand-name { font-weight: 800; font-size: 24px; line-height: 1.15; color: #111; }
  .headline {
    position: absolute; left: 551px; top: 97px; width: 517px; text-align: center;
    font-family: "Oswald", sans-serif; font-weight: 700; font-size: 40px; letter-spacing: 0.5px;
  }
  .headline sup { font-size: 20px; }
  .headline .accent { color: var(--green); }
  .save {
    position: absolute; left: 621px; top: 204px;
    font-weight: 900; font-size: 101px; letter-spacing: -2px; line-height: 1;
  }
  .first-month {
    position: absolute; left: 623px; top: 308px;
    font-size: 22px; color: var(--green); letter-spacing: 0.3px;
  }
  .percent-value {
    position: absolute; left: 929px; top: 188px;
    font-family: "Oswald", sans-serif; font-weight: 700; font-size: 150px; line-height: 1; color: var(--green);
  }
  .percent-sign {
    position: absolute; left: 1070px; top: 286px;
    font-weight: 800; font-size: 40px; line-height: 1;
  }
  .how-title {
    position: absolute; left: 739px; top: 379px; width: 200px; text-align: center;
    font-weight: 700; font-size: 27px; white-space: nowrap;
  }
  .step {
    position: absolute; top: 429px; width: 170px; height: 170px;
    display: flex; flex-direction: column; align-items: center; justify-content: center;
  }
  .step-icon { width: 70px; height: 62px; border-radius: 10px; margin-top: 10px; margin-bottom: 8px; }
  .icon-dog { background: linear-gradient(160deg, #ffffff 30%, #b0643a 100%); box-shadow: inset 0 0 0 1px #ddd; }
  .icon-cattle { background: #1b1b1b; }
  .icon-box { background: linear-gradient(160deg, #dcb77c, #b98a4b); }
  .step-caption {
    font-family: "Josefin Slab", serif; font-weight: 600; font-size: 13px; line-height: 1.25;
    text-align: center; width: 120px;
  }
  .step-1 { left: 545px; }
  .step-2 { left: 743px; }
  .step-3 { left: 942px; }
  .join-button {
    position: absolute; left: 68px; top: 632px; width: 347px; height: 70px;
    border: 3px solid var(--white); border-radius: 36px;
    background: linear-gradient(180deg, #8fca4b, #6fae33);
    display: flex; align-items: center; justify-content: center;
    color: var(--white); font-weight: 900; font-size: 33px; letter-spacing: 0.5px;
  }
  .promo { position: absolute; left: 450px; top: 612px; color: var(--white); }
  .promo-label { font-size: 23px; letter-spacing: 1.5px; margin-left: 5px; }
  .promo-code { font-weight: 900; font-size: 38px; letter-spacing: 0.5px; line-height: 1.15; }
  .promo-note { font-size: 20px; letter-spacing: 1px; margin-left: 5px; }
  .site-link {
    position: absolute; left: 807px; top: 652px; width: 307px; height: 52px;
    border: 2px solid var(--white);
    display: flex; align-items: center; justify-content: center;
    color: var(--white); font-weight: 700; font-size: 22px; letter-spacing: 0.3px;
  }
</style>
</head>
<body>
<main class="postcard">
  <svg class="shapes" viewBox="0 0 1140 733" width="1140" height="733" aria-hidden="true">
    <path d="M78,560 L78,222 Q78,158 150,158 Q232,158 242,262 Q252,322 332,322 Q562,322 578,472 Q586,560 520,560 Z" fill="var(--blob)"/>
    <path d="M62,560 L62,214 Q62,138 150,138" fill="none" stroke="#d4dccf" stroke-width="1.5"/>
    <path d="M400,312 Q580,306 600,470" fill="none" stroke="#d4dccf" stroke-width="1.5"/>
    <rect x="0" y="558" width="1140" height="175" fill="var(--band)"/>
    <g stroke="var(--green)" stroke-width="3" fill="none" stroke-linecap="round">
      <path d="M513,38 L538,70 L527,38"/>
      <path d="M548,32 L555,75 L543,35"/>
      <path d="M515,92 L535,90"/>
      <path d="M519,120 L528,117"/>
    </g>
    <path d="M575,70 Q660,60 930,62 Q1020,64 1058,86 Q1075,110 1064,150 Q1052,182 1040,190 L1050,202 L1020,192 Q900,200 640,198 Q565,196 558,160 Q550,120 560,90 Q565,74 575,70 Z" fill="none" stroke="var(--bubble-line)" stroke-width="2"/>
    <g stroke="var(--green)" stroke-width="2">
      <line x1="641" y1="393" x2="695" y2="393"/>
      <line x1="972" y1="393" x2="1026" y2="393"/>
    </g>
    <rect x="700" y="502" width="60" height="24" fill="var(--green)"/>
    <rect x="898" y="502" width="60" height="24" fill="var(--green)"/>
    <g fill="var(--white)" stroke="var(--green)" stroke-width="3">
      <circle cx="630" cy="514" r="84"/>
      <circle cx="828" cy="514" r="84"/>
      <circle cx="1027" cy="514" r="84"/>
    </g>
    <circle cx="686" cy="445" r="24" fill="#e4e4e4"/>
  </svg>

  <div class="dogs-photo" role="img" aria-label="Photo of a tricolour shepherd dog and a pug wearing pink sunglasses and a bandana"></div>

  <div class="brand-seal">
    <div class="ring"><p class="brand-name">Tawny<br>Gnaw Guild</p></div>
  </div>

  <h1 class="headline">TRY YOUR 1<sup>st</sup> <span class="accent">SUBSCRIPTION</span></h1>
  <p class="save">SAVE</p>
  <p class="first-month">ON YOUR FIRST MONTH</p>
  <p class="percent-value">50</p>
  <p class="percent-sign">%</p>

  <h2 class="how-title">HOW IT WORKS</h2>
  <div class="step step-1">
    <div class="step-icon icon-dog" role="img" aria-label="Illustration of a happy terrier"></div>
    <p class="step-caption">Doggy joy guarantee</p>
  </div>
  <div class="step step-2">
    <div class="step-icon icon-cattle" role="img" aria-label="Premium quality cattle silhouette illustration"></div>
    <p class="step-caption">Sourced from free range cattle</p>
  </div>
  <div class="step step-3">
    <div class="step-icon icon-box" role="img" aria-label="Illustration of a cardboard shipping box"></div>
    <p class="step-caption">Shipped to your doorstep</p>
  </div>

  <div class="join-button">JOIN THE CLUB</div>
  <div class="promo">
    <p class="promo-label">USE CODE:</p>
    <p class="promo-code">TAWNYGNAW</p>
    <p class="promo-note">AT CHECKOUT</p>
  </div>
  <div class="site-link">tawnygnawguild.com</div>
</main>
</body>
</html>
```